Web Design for Webdesign company 3 page PSD

Project
---------
We need a PSD Web Design to be used in a WordPress installation.
What we would like to create is a professional looking website for a web design agency. We also need you to look for suitable stock images to be placed on these pages.
We need the design for:
Homepage
Landing page
Contact page
attached in the pages file you will find a file with more in depth details how these files should be build up.
We would like to see a desktop version and a mobile version of these pages
The website should have a 1100px width.
The mobile design should have 480px width.
The homepage should have a header slider about 450px high.
The slider is preferred full width and should have some images text and a button
Objectives
-------------
The main objective for the website is to get leads from customers in the form of a request for a quotation or a call or mail me back action. The most important action for the homepage is to link and navigate to our landing pages.
What we want to tell our visitors (our main products)
-------------------------------------------------------------------
- A website with no big investment but a monthly rate
- A successful website with no worries (a complete website, seo, hosting and a service contract for future customization is included for a monthly rate)
Color Scheme
------------
Use branding colors. You can find them in the branding.pdf file.
Additional colors:
White: #ffffff
Black: #181818
Company info
--------------
We are a starting web design / marketing agency based in The Netherlands and looking for the design of our website. Our services are (custom) webdesign, website marketing or combinations of both. Our main customer group is small business owners.
We sell websites but give the option to buy it with a lease contract.
A second product is a default website with a complete service: SEO, hosting and a service contract for a monthly rate.
Content:
-----------
If not available place Lorem Ipsum text.
There will come about 400 words of text on the landing pages
Design Competition
--------------------------
Since this is a designing competition we would like to see your creativity.
What you can expect from us is a lot of feedback 7 days a week with short response time.
You can send us the first sketchy mock ups of the homepage and we will give feedback based on these design. But we like your feedback or comments as well
Read the pages file for more in depth details how the pages should be designed

Target Market(s)
Small business owners in The Netherlands
Industry/Entity Type
It Company
Number of Pages Required
3 page
Requirements
Must have
- Homepage:
- Header slider with images, some text and a link to a custom page
- The slider should have 3 designed slides
- Landings page:
- Sidebar
- Action button for a request for a quotation
- Action button for a call me back action
- Action button for an appointment
- Contact form:
- Address details
- Contact form
Nice to have
- Homepage:
- Full width slider
- Testimonial block
- Blog items
Should not have
- Flash
- A to crowded design

```html
<!DOCTYPE html>
<html lang="en">
<head>
<meta charset="utf-8">
<title>Willow Grove Web Studio</title>
<link href="https://fonts.googleapis.com/css2?family=Raleway:wght@400;500;600;700&family=Open+Sans:ital,wght@0,400;0,600;0,700;1,400&display=swap" rel="stylesheet">
<style>
  :root {
    --teal: #2f7982;
    --teal-band: #45797f;
    --teal-dark: #2a6c74;
    --ink: #2b2b2b;
    --grey-band: #c3c3c3;
    --footer: #343434;
    --white: #ffffff;
    --black: #181818;
  }
  * { box-sizing: border-box; margin: 0; padding: 0; }
  html, body { width: 803px; height: 1200px; overflow: hidden; background: var(--white); }
  body { position: relative; font-family: "Open Sans", sans-serif; color: var(--ink); }
  .abs { position: absolute; }

  /* Hero */
  .hero { left: 0; top: 0; width: 803px; height: 314px;
    background: linear-gradient(120deg, #e6e4e1 0%, #efeeec 45%, #e9e7e4 100%); }
  .hero-photo { left: 0; top: 0; width: 803px; height: 314px;
    background: radial-gradient(ellipse 140px 90px at 30px 170px, rgba(140,40,40,.25), transparent 70%),
                radial-gradient(ellipse 170px 80px at 400px 300px, rgba(232,150,40,.55), transparent 70%),
                radial-gradient(ellipse 90px 60px at 740px 270px, rgba(60,40,30,.25), transparent 70%),
                radial-gradient(ellipse 60px 90px at 780px 40px, rgba(40,40,40,.3), transparent 70%); }
  .hero-title { left: 40px; width: 436px; top: 38px; text-align: center;
    font-family: "Raleway", sans-serif; font-weight: 700; font-size: 35px; line-height: 43px; color: var(--teal); }
  .hero-text { left: 40px; width: 436px; top: 139px; text-align: center; font-size: 13px; line-height: 21px; color: var(--black); }
  .btn-more { left: 208px; top: 202px; width: 113px; height: 34px; background: var(--teal); color: var(--white);
    font-size: 11px; font-weight: 700; display: flex; align-items: center; justify-content: center; }
  .laptop-shot { left: 452px; top: 46px; width: 282px; height: 166px; border-radius: 6px 6px 2px 2px;
    background: linear-gradient(160deg, #1c1c1c 0%, #2f4f6f 40%, #2a8fd3 75%, #1a1a1a 100%); }

  /* Tagline */
  .tagline { left: 0; width: 803px; top: 340px; text-align: center; font-family: "Raleway", sans-serif; font-size: 21px; color: #333; }
  .btn-pill { left: 334px; top: 384px; width: 152px; height: 34px; border-radius: 17px; background: var(--teal);
    color: var(--white); font-family: "Raleway", sans-serif; font-size: 15px; display: flex; align-items: center; justify-content: center; gap: 10px; }

  /* Navigation */
  .navbar { left: 0; top: 446px; width: 803px; height: 84px; background: var(--teal-band); }
  .brand { left: 54px; top: 54px; color: var(--white); font-family: "Raleway", sans-serif; font-weight: 700; font-size: 11px; line-height: 13px; }
  .brand small { display: block; font-size: 7px; font-weight: 700; }
  .brand-dot { left: 80px; top: 10px; width: 36px; height: 36px; border-radius: 50%; background: #3a6b54; }
  .nav-item { top: 480px; color: var(--white); font-family: "Raleway", sans-serif; font-size: 13px; }
  .nav-active { border-top: 1px solid var(--white); border-bottom: 1px solid var(--white); padding: 13px 2px; top: 466px; }

  /* Welcome */
  .welcome { left: 0; top: 530px; width: 803px; height: 167px; background: var(--grey-band); }
  .welcome-title { left: 53px; top: 565px; font-family: "Raleway", sans-serif; font-size: 24px; color: var(--white); }
  .welcome-title span { color: var(--teal); }
  .rule { height: 2px; width: 34px; background: var(--white); }
  .welcome-text { left: 53px; top: 615px; width: 390px; font-size: 8.8px; line-height: 17.6px; color: var(--white); }
  .tools-art { left: 462px; top: 544px; width: 290px; height: 148px; border-radius: 8px;
    background: linear-gradient(90deg, #d8b07a 0%, #e8c24a 45%, #cfd3d6 70%, #d9534f 100%); opacity: .8; }

  /* Blog & testimonials */
  .section-title { top: 722px; font-family: "Raleway", sans-serif; font-size: 21px; color: var(--ink); }
  .section-rule { top: 753px; height: 2px; width: 34px; background: var(--teal); }
  .post-thumb { left: 52px; width: 58px; height: 58px; }
  .post-text { left: 120px; width: 270px; font-size: 10px; line-height: 17px; color: var(--ink); }
  .post-date { left: 124px; font-size: 9px; font-style: italic; color: #777; display: flex; align-items: center; gap: 5px; }
  .quote-box { left: 410px; top: 774px; width: 342px; height: 84px; border: 1px solid #8fb3b8; border-radius: 3px; }
  .quote-text { left: 447px; top: 787px; width: 280px; font-size: 9.6px; line-height: 18px; color: var(--ink); }
  .quote-mark { font-family: Georgia, serif; font-style: italic; font-weight: 700; color: var(--teal); font-size: 16px; }
  .avatar { left: 546px; top: 874px; width: 56px; height: 56px; border-radius: 50%;
    background: radial-gradient(circle at 50% 40%, #b9b2ab, #5a5a5a); }
  .person-name { left: 473px; width: 200px; top: 935px; text-align: center; font-size: 10px; font-weight: 700; color: var(--teal); }
  .person-role { left: 473px; width: 200px; top: 952px; text-align: center; font-size: 8px; font-style: italic; color: #555; }
  .dot { top: 986px; width: 15px; height: 4px; background: #9a9a9a; }

  /* Footer */
  .footer { left: 0; top: 1025px; width: 803px; height: 140px; background: var(--footer); }
  .footer-title { top: 1041px; font-family: "Raleway", sans-serif; font-size: 13px; color: var(--white); }
  .footer-text { left: 87px; font-size: 10px; line-height: 18px; color: #e8e8e8; }
  .icon-ring { width: 28px; height: 28px; border-radius: 50%; border: 1.5px solid var(--white); display: flex; align-items: center; justify-content: center; }
  .search { left: 290px; top: 1071px; width: 223px; height: 35px; background: var(--teal); display: flex; align-items: center; justify-content: space-between; padding: 0 12px 0 15px; color: var(--white); font-size: 8px; }
  .social { top: 1071px; width: 28px; height: 28px; border-radius: 50%; border: 1.5px solid var(--white); }
  .social.on { background: var(--teal-dark); border-color: var(--teal-dark); }
  .copyright { left: 0; top: 1165px; width: 803px; height: 35px; background: var(--teal-band); color: var(--white);
    font-family: "Raleway", sans-serif; font-size: 9px; display: flex; align-items: center; justify-content: center; }
  .copyright u { margin: 0 2px; }
</style>
</head>
<body>

<section class="hero abs">
  <div class="hero-photo abs" role="img" aria-label="Desk flat-lay photo with rope, wallet, orange sneakers and glasses"></div>
  <h1 class="hero-title abs">A website from €19,95 per month</h1>
  <p class="hero-text abs">With us, you can lease a website. So no big investment upfront.<br>A website is available from € 19.95 per month</p>
  <a class="btn-more abs">More Information</a>
  <div class="laptop-shot abs" role="img" aria-label="Laptop showing a sample website"></div>
</section>

<p class="tagline abs">Sparking creative ideas to optimise your brands.</p>
<a class="btn-pill abs">
  <svg width="18" height="20" viewBox="0 0 18 20"><path d="M16 1C6 2 2 8 3 16l-2 3M3 16C11 15 16 9 16 1" fill="var(--white)" stroke="var(--white)" stroke-width="1.2"/></svg>
  Web Design
</a>

<nav class="navbar abs">
  <div class="brand-dot abs"></div>
  <div class="brand abs">WILLOW GROVE<small>WEB STUDIO</small></div>
</nav>
<span class="nav-item nav-active abs" style="left:327px">Home</span>
<span class="nav-item abs" style="left:399px">About</span>
<span class="nav-item abs" style="left:468px">Web design</span>
<span class="nav-item abs" style="left:572px">Services</span>
<span class="nav-item abs" style="left:654px">Contact</span>

<section class="welcome abs">
  <div class="tools-art abs" style="top:14px" role="img" aria-label="Illustration of a browser globe, design monitor and pencil cup"></div>
</section>
<h2 class="welcome-title abs">Welcome to <span>WILLOW GROVE</span></h2>
<div class="rule abs" style="left:53px;top:599px"></div>
<p class="welcome-text abs">Lorem Ipsum is simply dummy text of the printing and typesetting industry. Lorem Ipsum has been the industry's standard dummy text ever since the 1500s, when an unknown printer took a galley of type and scrambled it to make a type specimen book. It has survived not.</p>

<h2 class="section-title abs" style="left:53px">Latest Blog Posts</h2>
<div class="section-rule abs" style="left:53px"></div>
<h2 class="section-title abs" style="left:411px">Testimonials</h2>
<div class="section-rule abs" style="left:411px"></div>

<div class="post-thumb abs" style="top:774px;background:linear-gradient(135deg,#6d8aa5,#d9c9bd)" role="img" aria-label="Hand touching a screen"></div>
<p class="post-text abs" style="top:776px">Lorem Ipsum has been the industry's standard dummy text ever since the 1500s.</p>
<div class="post-date abs" style="top:816px"><svg width="9" height="9" viewBox="0 0 9 9"><rect x=".5" y="1.5" width="8" height="7" fill="none" stroke="var(--teal)"/><rect x=".5" y="1.5" width="8" height="2" fill="var(--teal)"/></svg>03.11.2014</div>

<div class="post-thumb abs" style="top:857px;background:linear-gradient(135deg,#cfe1ea,#8fb0c4)" role="img" aria-label="Tablet showing charts"></div>
<p class="post-text abs" style="top:858px">Lorem Ipsum has been the industry's standard dummy text ever since the 1500s.</p>
<div class="post-date abs" style="top:899px"><svg width="9" height="9" viewBox="0 0 9 9"><rect x=".5" y="1.5" width="8" height="7" fill="none" stroke="var(--teal)"/><rect x=".5" y="1.5" width="8" height="2" fill="var(--teal)"/></svg>03.11.2014</div>

<div class="post-thumb abs" style="top:938px;background:linear-gradient(135deg,#f2f2f2,#c9cdd1)" role="img" aria-label="Hand writing on paper"></div>
<p class="post-text abs" style="top:940px">Lorem Ipsum has been the industry's standard dummy text ever since the 1500s.</p>
<div class="post-date abs" style="top:981px"><svg width="9" height="9" viewBox="0 0 9 9"><rect x=".5" y="1.5" width="8" height="7" fill="none" stroke="var(--teal)"/><rect x=".5" y="1.5" width="8" height="2" fill="var(--teal)"/></svg>03.11.2014</div>

<div class="quote-box abs"></div>
<svg class="abs" style="left:566px;top:857px" width="16" height="9" viewBox="0 0 16 9"><path d="M0 0L8 8L16 0" fill="var(--white)" stroke="#8fb3b8"/></svg>
<span class="quote-mark abs" style="left:425px;top:785px">“</span>
<p class="quote-text abs">I'd have to say Marissa is the most efficient, easy going, web designer out there. She communicates effectively and gets the job done <span class="quote-mark">”</span></p>
<div class="avatar abs" role="img" aria-label="Client portrait"></div>
<p class="person-name abs">John Doe</p>
<p class="person-role abs">Designer, brightframe</p>
<div class="dot abs" style="left:548px;background:var(--black)"></div>
<div class="dot abs" style="left:566px"></div>
<div class="dot abs" style="left:584px"></div>

<footer class="footer abs"></footer>
<h3 class="footer-title abs" style="left:53px">Contact Info</h3>
<h3 class="footer-title abs" style="left:291px">Search</h3>
<h3 class="footer-title abs" style="left:558px">Get Social</h3>

<div class="icon-ring abs" style="left:52px;top:1067px">
  <svg width="14" height="12" viewBox="0 0 14 12"><path d="M7 0L0 6h2v6h4V8h2v4h4V6h2z" fill="var(--white)"/></svg>
</div>
<p class="footer-text abs" style="top:1070px">Willow Grove<br>254, Office area name,City,Country</p>
<div class="icon-ring abs" style="left:52px;top:1113px">
  <svg width="13" height="13" viewBox="0 0 13 13"><path d="M3 1l2 3-1.5 1.5c.8 1.8 2.2 3.2 4 4L9 8l3 2-1.5 2.5C6 12 1 7 .5 2.5z" fill="var(--white)"/></svg>
</div>
<p class="footer-text abs" style="top:1115px">Phone No. : + 123 456 7890</p>
<p class="footer-text abs" style="top:1136px">Email : info@willowgrove.com</p>

<div class="search abs">Search Keyword....
  <svg width="14" height="14" viewBox="0 0 14 14"><circle cx="6" cy="6" r="4.5" fill="none" stroke="var(--white)" stroke-width="2"/><path d="M9.3 9.3L13 13" stroke="var(--white)" stroke-width="2.2"/></svg>
</div>

<div class="social on abs" style="left:557px" aria-label="Social profile 1"></div>
<div class="social abs" style="left:589px" aria-label="Social profile 2"></div>
<div class="social abs" style="left:620px" aria-label="Social profile 3"></div>
<div class="social abs" style="left:651px" aria-label="Social profile 4"></div>
<div class="social abs" style="left:682px" aria-label="News feed"></div>

<div class="copyright abs">© 2015 <u>Willow Grove</u>. All Rights Reserved.</div>

</body>
</html>
```